Tobin's Jewelry Studio Needs a Moving Location Flyer

We need a flyer to inform our customers of our location moving. We will be moving to our city's downtown which is only 1 mile away from our current address. We will be having a moving sale ( Up to 80% off). The sale starts Sept. 8th Our business creates, sells, and repairs fine jewelry. Dimensions are 5"x8"

Target Market(s)

Women ages 25-55

Industry/Entity Type

Jewelry

Colors
85abd2
cfdeed

Requirements
Must have
• Our logo
• Mention of the sale
• Our current address
• 4187 Marsh Creek Blvd.
• Brookhollow, Ca 91642
• (909)417-2863
Nice to have
• Mention that we're relocating to downtown Brookhollow (new location opening Nov. 1st.)

```html
<!DOCTYPE html>
<html lang="en">
<head>
<meta charset="utf-8">
<title>Tobin's Jewelry Studio – Moving Sale</title>
<link rel="stylesheet" href="https://fonts.googleapis.com/css2?family=Playfair+Display:wght@400;600;700&display=swap">
<style>
  :root {
    --sky: #bce3e8;
    --paper: #ffffff;
    --ink: #3a3a3a;
    --rule: #2c2c2c;
  }
  html, body {
    margin: 0;
    padding: 0;
    overflow: hidden;
    background: var(--paper);
  }
  .flyer {
    position: relative;
    width: 1200px;
    height: 913px;
    overflow: hidden;
    background: var(--paper);
    font-family: "Playfair Display", Georgia, serif;
    color: var(--ink);
  }
  .flyer__shapes {
    position: absolute;
    inset: 0;
  }
  .t {
    position: absolute;
    transform: translate(-50%, -50%);
    white-space: nowrap;
    text-align: center;
    line-height: 1;
  }
  .brand-name {
    left: 592px; top: 57px;
    font-size: 17px;
    font-weight: 600;
    letter-spacing: 0.02em;
  }
  .sale__moving {
    left: 592px; top: 239px;
    font-size: 50px;
    letter-spacing: 0.16em;
    padding-left: 0.16em;
  }
  .sale__word {
    left: 592px; top: 330px;
    font-size: 178px;
    letter-spacing: 0.01em;
  }
  .sale__upto {
    left: 592px; top: 432px;
    font-size: 32px;
    letter-spacing: 0.2em;
    padding-left: 0.2em;
  }
  .sale__amount {
    left: 592px; top: 500px;
    display: flex;
    align-items: center;
  }
  .sale__number {
    font-size: 96px;
    font-weight: 700;
  }
  .sale__unit {
    display: flex;
    flex-direction: column;
    align-items: flex-start;
    margin-left: 8px;
    margin-top: 6px;
  }
  .sale__percent { font-size: 30px; }
  .sale__off {
    font-size: 30px;
    letter-spacing: 0.2em;
    margin-top: 2px;
  }
  .start__label {
    left: 802px; top: 483px;
    font-size: 17px;
    font-weight: 700;
  }
  .start__date {
    left: 802px; top: 508px;
    font-size: 25px;
  }
  .info__heading {
    top: 643px;
    font-size: 28px;
    font-weight: 700;
    letter-spacing: 0.28em;
    padding-left: 0.28em;
  }
  .info__text { font-size: 22px; }
  .info__address { font-size: 18px; }
  .info__phone { font-size: 30px; }
  .col-left { left: 328px; }
  .col-right { left: 875px; }
  .specialty {
    left: 600px;
    font-size: 18px;
    letter-spacing: 0.42em;
    padding-left: 0.42em;
  }
</style>
</head>
<body>
<main class="flyer">
  <svg class="flyer__shapes" width="1200" height="913" viewBox="0 0 1200 913" aria-hidden="true">
    <rect class="top-band" x="0" y="0" width="1200" height="491" fill="var(--sky)"/>
    <circle class="brand-cap" cx="592" cy="-34" r="199" fill="var(--paper)"/>
    <g fill="none" stroke="var(--rule)" stroke-width="2">
      <line x1="45" y1="57" x2="440" y2="57"/>
      <line x1="744" y1="57" x2="1157" y2="57"/>
      <line x1="45" y1="57" x2="45" y2="869"/>
      <line x1="1157" y1="57" x2="1157" y2="869"/>
      <line x1="45" y1="869" x2="1157" y2="869"/>
    </g>
    <circle cx="592" cy="358" r="258" fill="var(--paper)"/>
    <circle cx="592" cy="358" r="250" fill="var(--sky)"/>
    <circle cx="802" cy="499" r="75" fill="var(--paper)"/>
    <circle cx="802" cy="499" r="69" fill="var(--sky)"/>
    <g stroke="var(--rule)" stroke-width="1.5" fill="var(--rule)">
      <line x1="80" y1="671" x2="576" y2="671"/>
      <circle cx="328" cy="671" r="3"/>
      <line x1="626" y1="671" x2="1122" y2="671"/>
      <circle cx="874" cy="671" r="3"/>
      <line x1="595" y1="633" x2="595" y2="746"/>
    </g>
  </svg>

  <div class="t brand-name">Tobin's Jewelry Studio</div>

  <div class="t sale__moving">MOVING</div>
  <div class="t sale__word">SALE</div>
  <div class="t sale__upto">UP TO</div>
  <div class="t sale__amount">
    <span class="sale__number">80</span>
    <span class="sale__unit">
      <span class="sale__percent">%</span>
      <span class="sale__off">OFF</span>
    </span>
  </div>

  <div class="t start__label">STARTS</div>
  <div class="t start__date">Sept. 8th</div>

  <div class="t info__heading col-left">WE ARE MOVING</div>
  <div class="t info__text col-left" style="top:697px">to Downtown Brookhollow</div>
  <div class="t info__text col-left" style="top:730px">New location opening in November</div>

  <div class="t info__heading col-right">CURRENT LOCATION</div>
  <div class="t info__address col-right" style="top:697px">4187 Marsh Creek Blvd. Brookhollow, Ca 91642</div>
  <div class="t info__phone col-right" style="top:732px">(909)417-2863</div>

  <div class="t specialty" style="top:814px">SPECIALIZING IN</div>
  <div class="t specialty" style="top:845px">CUSTOM DESIGN, REPAIRS &amp; FINE JEWELRY</div>
</main>
</body>
</html>
```